Infectious Diseases Research Laboratory Needs Business Card

We need a business card for an academic research laboratory based in Kansas City called MORVEK. The full lab name is Microbial Dose-Response/Exposure Bridging Studies Laboratory, but this does not need to be incorporated. We study novel ways to optimize the treatment of multidrug-resistant bacterial infections ("superbugs") throughout the entire biomedical research spectrum (from benchtop to bedside). The name MORVEK is not only an acronym for our lab name, but also represents our desire to make discoveries and explore the unknown (the stars, if you well). It also serves as an ode to the state of Kansas motto where we are based, ad astra per aspera ("to the stars, through difficulty").

Target Market(s)

Pharmaceutical companies, researchers

Industry/Entity Type

Pharmaceutical

Contact Information for Business Card

The business card should incorporate and complement our new logo (see uploaded files). Double-sided designs are preferred. Looking for something modern, but professional.

Font styles to use
Sans Serif

Requirements
Must have
• Double-sided. One side would ideally be a solid color incorporating logo and the other should also have the logo (smaller), but incorporate staff information.
• Color codes:
• Red: #F04C51
• Blue: #3477B5
• Gray: #808285

```html
<!DOCTYPE html>
<html lang="en">
<head>
<meta charset="utf-8">
<title>MORVEK Business Card</title>
<link rel="stylesheet" href="https://fonts.googleapis.com/css2?family=Arimo:wght@400;700&display=swap">
<style>
  :root {
    --charcoal: #454545;
    --charcoal-deep: #3c3c3c;
    --paper: #f4f4f2;
    --ink: #1e1e1e;
    --soft-text: #d6d6d6;
    --backdrop: #e6e4e0;
  }
  * { margin: 0; padding: 0; box-sizing: border-box; }
  html, body {
    width: 1200px; height: 799px; overflow: hidden;
    background: var(--backdrop);
    font-family: "Arimo", Arial, sans-serif;
  }
  .sheet {
    width: 1200px; height: 799px;
    display: flex; align-items: center; justify-content: center; gap: 40px;
  }
  .card {
    width: 540px; height: 309px; position: relative; overflow: hidden;
    box-shadow: 0 6px 18px rgba(0,0,0,0.18);
  }

  /* Back: contact side */
  .card--contact { display: flex; background: var(--paper); }
  .contact-brand {
    width: 44%; display: flex; align-items: center; justify-content: center;
  }
  .contact-panel {
    width: 56%; background: var(--charcoal); color: #fff;
    padding: 30px 24px 0 30px;
  }
  .holder-name { font-size: 21px; font-weight: 400; letter-spacing: 0.2px; }
  .holder-role { font-size: 12px; color: var(--soft-text); margin: 3px 0 0 20px; }
  .contact-list { list-style: none; margin-top: 22px; }
  .contact-list li {
    display: flex; align-items: center; gap: 18px;
    font-size: 12.5px; height: 32px; color: #f2f2f2;
  }
  .contact-list svg { width: 16px; height: 16px; flex: none; }

  .wordmark {
    display: flex; align-items: center; gap: 10px;
    color: var(--ink); font-weight: 400; letter-spacing: 3px;
  }
  .wordmark__dot { border-radius: 50%; background: var(--ink); flex: none; }
  .wordmark--small { font-size: 26px; }
  .wordmark--small .wordmark__dot { width: 18px; height: 18px; }

  /* Front: brand side */
  .card--front {
    background: var(--charcoal-deep); padding: 12px;
  }
  .front-field {
    background: var(--paper); height: 100%; display: flex; flex-direction: column;
  }
  .front-logo-area { flex: 1; display: flex; align-items: center; justify-content: center; }
  .wordmark--large { font-size: 46px; letter-spacing: 5px; gap: 18px; }
  .wordmark--large .wordmark__dot { width: 34px; height: 34px; }
  .front-band {
    height: 66px; background: var(--charcoal); color: var(--soft-text);
    display: flex; align-items: center; justify-content: center;
    font-size: 14px; letter-spacing: 0.3px;
  }
</style>
</head>
<body>
<main class="sheet">

  <section class="card card--contact" aria-label="Card back with contact details">
    <div class="contact-brand">
      <div class="wordmark wordmark--small"><span class="wordmark__dot"></span>MORVEK</div>
    </div>
    <div class="contact-panel">
      <h1 class="holder-name">Lena Hartwell</h1>
      <p class="holder-role">Research executive</p>
      <ul class="contact-list">
        <li>
          <svg viewBox="0 0 16 16" fill="none" stroke="#fff" stroke-width="1.3"><path d="M8 15s5-5 5-8.5A5 5 0 0 0 3 6.5C3 10 8 15 8 15z"/><circle cx="8" cy="6.5" r="1.8"/></svg>
          418 Orchard Lane, USA
        </li>
        <li>
          <svg viewBox="0 0 16 16" fill="#fff"><path d="M1 6c0-2 3-3 7-3s7 1 7 3v1h-4V5.5H5V7H1z"/><rect x="3" y="8" width="10" height="6" rx="1"/></svg>
          210.555.014.382
        </li>
        <li>
          <svg viewBox="0 0 16 16" fill="#fff"><path d="M4 1l2.5 3-1.5 2a8 8 0 0 0 5 5l2-1.5 3 2.5-1.5 2.5C7 15 1 9 1.5 3z"/></svg>
          210.555.019.647
        </li>
        <li>
          <svg viewBox="0 0 16 16" fill="none" stroke="#fff" stroke-width="1.2"><circle cx="8" cy="8" r="6.5"/><ellipse cx="8" cy="8" rx="3" ry="6.5"/><path d="M1.5 8h13M2.5 4.5h11M2.5 11.5h11"/></svg>
          www.morvek.com
        </li>
        <li>
          <svg viewBox="0 0 16 16" fill="none" stroke="#fff" stroke-width="1.3"><rect x="1.5" y="3.5" width="13" height="9" rx="1"/><path d="M1.5 4l6.5 5 6.5-5"/></svg>
          info@morvek.com
        </li>
      </ul>
    </div>
  </section>

  <section class="card card--front" aria-label="Card front with brand name">
    <div class="front-field">
      <div class="front-logo-area">
        <div class="wordmark wordmark--large"><span class="wordmark__dot"></span>MORVEK</div>
      </div>
      <div class="front-band">Research Lab</div>
    </div>
  </section>

</main>
</body>
</html>
```